Bref créative
business cards & stationary
Corvell Insulation
Modern
BO KERRIGAN
SALESMAN
14 PELLMORE CT.
LARKDALE, CA 95990
bo.kerrigan@corvellinsulation.com
www.corvellinsulation.com
I'd like the edges to be rounded instead of pointed. I would also like little symbols next to the phone, E-mail, website, and fax. For example, near the phone number, a small telephone. Also, if possible, I would like a QR Barcode that leads to my website on the back.

```html
<!DOCTYPE html>
<html lang="en">
<head>
<meta charset="utf-8">
<title>Corvell Insulation – Business Card</title>
<link href="https://fonts.googleapis.com/css2?family=Exo+2:wght@400;600;700&family=Michroma&display=swap" rel="stylesheet">
<style>
  :root {
    --page-bg: #e9ebe7;
    --card-top: #fbfcfb;
    --card-edge: #d9dcd8;
    --ink-dark: #3b3f3e;
    --brand-green: #5aab2c;
    --band-light: #8fd14b;
    --band-mid: #5eb22c;
    --band-deep: #3f8f1f;
    --panel-dark: rgba(30, 60, 20, 0.35);
    --notch: #2f3432;
    --silver-light: #f4f5f4;
    --silver-dark: #a9adab;
    --text-light: #f3f8ee;
    --icon-bg: #2d3a2a;
  }
  html, body {
    margin: 0;
    width: 1200px;
    height: 768px;
    overflow: hidden;
    background: var(--page-bg);
  }
  .canvas {
    position: relative;
    width: 1200px;
    height: 768px;
  }
  .business-card {
    position: absolute;
    left: 100px;
    top: 98px;
    width: 1000px;
    height: 572px;
    border-radius: 28px;
    overflow: hidden;
    background: linear-gradient(180deg, var(--card-top) 0%, #f1f3f1 100%);
    box-shadow: 0 18px 40px rgba(0,0,0,0.18), 0 0 0 1px var(--card-edge);
  }
  .brand {
    position: absolute;
    top: 82px;
    left: 0;
    right: 0;
    display: flex;
    justify-content: center;
    align-items: center;
    gap: 22px;
  }
  .brand-square {
    width: 64px;
    height: 64px;
    background: var(--brand-green);
    border-radius: 6px;
  }
  .brand-name {
    font-family: "Exo 2", sans-serif;
    font-weight: 700;
    font-size: 58px;
    letter-spacing: 2px;
    color: var(--ink-dark);
    text-transform: uppercase;
    line-height: 1;
  }
  .info-band {
    position: absolute;
    left: 0;
    right: 0;
    top: 262px;
    height: 200px;
    background: radial-gradient(ellipse at 35% 40%, var(--band-light) 0%, var(--band-mid) 45%, var(--band-deep) 100%);
  }
  .info-band::after {
    content: "";
    position: absolute;
    top: 0; bottom: 0; right: 0;
    width: 470px;
    background: linear-gradient(90deg, rgba(0,0,0,0) 0%, var(--panel-dark) 25%, var(--panel-dark) 100%);
  }
  .notch {
    position: absolute;
    left: 118px;
    top: 262px;
    width: 0;
    height: 0;
    border-left: 16px solid transparent;
    border-right: 16px solid transparent;
    border-top: 16px solid var(--notch);
    z-index: 2;
  }
  .silver-strip {
    position: absolute;
    left: 0;
    right: 0;
    top: 462px;
    height: 34px;
    background: linear-gradient(180deg, var(--silver-dark) 0%, var(--silver-light) 45%, #c8cbc9 100%);
  }
  .person {
    position: absolute;
    left: 108px;
    top: 298px;
    font-family: "Michroma", sans-serif;
    color: var(--text-light);
    z-index: 2;
  }
  .person-name {
    font-size: 19px;
    letter-spacing: 1px;
    margin: 0 0 6px;
  }
  .person-title {
    font-size: 14px;
    letter-spacing: 1px;
    margin: 0;
    opacity: 0.9;
  }
  .contact-list {
    position: absolute;
    left: 578px;
    top: 272px;
    margin: 0;
    padding: 0;
    list-style: none;
    z-index: 2;
    font-family: "Michroma", sans-serif;
    font-size: 12.5px;
    letter-spacing: 0.5px;
    color: var(--text-light);
  }
  .contact-list li {
    display: flex;
    align-items: center;
    gap: 12px;
    height: 26px;
  }
  .contact-icon {
    width: 18px;
    height: 18px;
    flex: none;
  }
  .contact-icon.blank { visibility: hidden; }
</style>
</head>
<body>
<div class="canvas">
  <div class="business-card">
    <div class="brand">
      <div class="brand-square"></div>
      <div class="brand-name">Corvell Insulation</div>
    </div>

    <div class="info-band"></div>
    <div class="notch"></div>
    <div class="silver-strip"></div>

    <div class="person">
      <p class="person-name">BO KERRIGAN</p>
      <p class="person-title">SALESMAN</p>
    </div>

    <ul class="contact-list">
      <li>
        <svg class="contact-icon" viewBox="0 0 18 18"><circle cx="9" cy="9" r="9" fill="#2d3a2a"/><path d="M9 4a3 3 0 0 0-3 3c0 2.3 3 6 3 6s3-3.7 3-6a3 3 0 0 0-3-3z" fill="#fff"/><circle cx="9" cy="7" r="1.1" fill="#2d3a2a"/></svg>
        <span>14 PELLMORE CT.</span>
      </li>
      <li>
        <svg class="contact-icon blank" viewBox="0 0 18 18"></svg>
        <span>LARKDALE, CA 95990</span>
      </li>
      <li>
        <svg class="contact-icon" viewBox="0 0 18 18"><circle cx="9" cy="9" r="9" fill="#2d3a2a"/><path d="M6 4.5l2 2-1 1.2c.6 1.3 1.5 2.2 2.8 2.8l1.2-1 2 2-1.3 1.5C8.8 12.8 5.2 9.2 4.5 6.3z" fill="#fff"/></svg>
        <span>(530) 555-0142</span>
      </li>
      <li>
        <svg class="contact-icon" viewBox="0 0 18 18"><circle cx="9" cy="9" r="9" fill="#2d3a2a"/><rect x="6.3" y="3.8" width="5.4" height="10.4" rx="1" fill="#fff"/><rect x="7.2" y="5" width="3.6" height="6.5" fill="#2d3a2a"/></svg>
        <span>(530) 555-0178</span>
      </li>
      <li>
        <svg class="contact-icon" viewBox="0 0 18 18"><circle cx="9" cy="9" r="9" fill="#2d3a2a"/><rect x="6" y="4" width="6" height="3.5" fill="#fff"/><rect x="4" y="7.5" width="10" height="4.5" rx="1" fill="#fff"/><rect x="6" y="11" width="6" height="3" fill="#fff" stroke="#2d3a2a" stroke-width="0.6"/></svg>
        <span>(530) 555-0193</span>
      </li>
      <li>
        <svg class="contact-icon" viewBox="0 0 18 18"><circle cx="9" cy="9" r="9" fill="#2d3a2a"/><rect x="4" y="5.5" width="10" height="7" rx="0.8" fill="#fff"/><path d="M4.3 6l4.7 3.8L13.7 6" fill="none" stroke="#2d3a2a" stroke-width="1"/></svg>
        <span>bo.kerrigan@corvellinsulation.com</span>
      </li>
      <li>
        <svg class="contact-icon" viewBox="0 0 18 18"><circle cx="9" cy="9" r="9" fill="#2d3a2a"/><circle cx="9" cy="9" r="4.8" fill="none" stroke="#fff" stroke-width="1"/><ellipse cx="9" cy="9" rx="2" ry="4.8" fill="none" stroke="#fff" stroke-width="1"/><line x1="4.2" y1="9" x2="13.8" y2="9" stroke="#fff" stroke-width="1"/></svg>
        <span>www.corvellinsulation.com</span>
      </li>
    </ul>
  </div>
</div>
</body>
</html>
```